CareLumen business cards

We need a business card design that we could customize as needed for employees. We will need space for Name, Title, 1-2 phone numbers and email address.

We are a Pharmacy Benefits Management (PBM) company for hospice agencies and beginning a nationwide expansion. Attached is a vector file of our logo.

Cards can be single or double sided.

```html
<!DOCTYPE html>
<html lang="en">
<head>
<meta charset="utf-8">
<title>CareLumen Business Cards</title>
<link rel="stylesheet" href="https://fonts.googleapis.com/css2?family=Open+Sans:wght@400;700&display=swap">
<style>
  :root {
    --backdrop: #2a2a2a;
    --card: #ffffff;
    --leaf: #9bcc66;
    --ink-blue: #1f5fa6;
    --rule: #c8d8b8;
  }
  * { margin: 0; padding: 0; box-sizing: border-box; }
  html, body {
    width: 1200px;
    height: 900px;
    overflow: hidden;
    background: var(--backdrop);
    font-family: "Open Sans", Arial, sans-serif;
  }
  .sheet {
    position: relative;
    width: 1200px;
    height: 900px;
  }
  .card {
    position: absolute;
    left: 285px;
    width: 630px;
    height: 360px;
    background: var(--card);
    overflow: hidden;
  }
  .card--back { top: 50px; }
  .card--front { top: 490px; }

  .band {
    position: absolute;
    background: var(--leaf);
  }
  .wordmark {
    position: absolute;
    display: flex;
    align-items: center;
    gap: 10px;
  }
  .wordmark__square {
    width: 34px;
    height: 34px;
    background: var(--leaf);
  }
  .wordmark__name {
    font-size: 34px;
    font-weight: 400;
    color: var(--ink-blue);
    letter-spacing: -0.5px;
    white-space: nowrap;
  }

  /* back side */
  .card--back .wordmark { left: 215px; top: 150px; }
  .card--back .band--long { left: 0; top: 245px; width: 300px; height: 62px; }
  .card--back .band--tab { right: 0; top: 145px; width: 70px; height: 40px; }

  /* front side */
  .card--front .wordmark { left: 40px; top: 104px; }
  .card--front .band--long { left: 0; top: 195px; width: 350px; height: 64px; }
  .card--front .band--tab { right: 0; top: 80px; width: 66px; height: 40px; }

  .person {
    position: absolute;
    left: 250px;
    width: 158px;
    top: 132px;
    text-align: right;
    font-weight: 700;
    line-height: 1.15;
    white-space: nowrap;
  }
  .person__name { font-size: 19px; color: var(--ink-blue); }
  .person__title { font-size: 19px; color: var(--leaf); }

  .divider {
    position: absolute;
    left: 420px;
    top: 110px;
    width: 1px;
    height: 82px;
    background: var(--rule);
  }
  .contact {
    position: absolute;
    left: 432px;
    top: 112px;
    width: 118px;
    font-size: 12px;
    color: var(--ink-blue);
    line-height: 1.3;
    text-align: center;
    white-space: nowrap;
  }
  .contact__email { font-size: 9.5px; }
</style>
</head>
<body>
<main class="sheet">
  <section class="card card--back" aria-label="Card back">
    <div class="band band--tab"></div>
    <div class="band band--long"></div>
    <div class="wordmark">
      <span class="wordmark__square"></span>
      <span class="wordmark__name">CareLumen</span>
    </div>
  </section>

  <section class="card card--front" aria-label="Card front">
    <div class="band band--tab"></div>
    <div class="band band--long"></div>
    <div class="wordmark">
      <span class="wordmark__square"></span>
      <span class="wordmark__name">CareLumen</span>
    </div>
    <div class="person">
      <div class="person__name">Daniel Rowe</div>
      <div class="person__title">CEO</div>
    </div>
    <div class="divider"></div>
    <div class="contact">
      <div>555.201.4837 (C)</div>
      <div>555.310.9264 (O)</div>
      <div class="contact__email">daniel@carelumen.com</div>
    </div>
  </section>
</main>
</body>
</html>
```